Stationary w/Bizz Card for Medical Equipment Company
Harborline Biomedical Systems
Stationary w/Bizz Card  for Medical Equipment Company - Health
Creative Brief
Professional
Derek Palmer
Vice President
415 Wexmoor Avenue Jacksonville, FL 32209
derek.palmer@hb-sysmed.net
www.hb-sysmed.net
Somewhere on the business card please put "Harborline Biomedical Systems"

```html
<!DOCTYPE html>
<html lang="en">
<head>
<meta charset="utf-8">
<title>Harborline Biomedical Systems – Business Cards</title>
<link href="https://fonts.googleapis.com/css2?family=Arimo:wght@400;700&family=Libre+Baskerville:wght@700&display=swap" rel="stylesheet">
<style>
  :root {
    --backdrop: #d9dadc;
    --card-light: #ffffff;
    --card-silver: #dfe2e6;
    --ink: #1d1d1f;
    --ink-soft: #3c3c40;
    --brand-blue: #1f8fd6;
    --brand-deep: #0a5fa8;
    --brand-pale: #9fd3f5;
  }
  * { margin: 0; padding: 0; box-sizing: border-box; }
  html, body { width: 1200px; height: 751px; overflow: hidden; }
  body {
    background: var(--backdrop);
    position: relative;
    font-family: "Arimo", Arial, sans-serif;
    color: var(--ink);
  }
  .card {
    position: absolute;
    border-radius: 22px;
    overflow: hidden;
    background: linear-gradient(160deg, var(--card-light) 0%, #f3f4f6 45%, var(--card-silver) 100%);
    box-shadow: 0 4px 14px rgba(0,0,0,.18);
  }
  .company-title {
    font-family: "Libre Baskerville", Georgia, serif;
    font-weight: 700;
    font-variant: small-caps;
    color: var(--ink);
    position: absolute;
  }
  .wordmark {
    position: absolute;
    display: flex;
    align-items: center;
    gap: 14px;
  }
  .wordmark-dot {
    border-radius: 50%;
    background: var(--brand-blue);
  }
  .wordmark-name {
    font-family: "Arimo", Arial, sans-serif;
    font-weight: 700;
    color: var(--brand-blue);
    letter-spacing: 2px;
  }

  /* Front card */
  .card-front { left: 343px; top: 36px; width: 516px; height: 319px; }
  .card-front .company-title { top: 20px; left: 0; width: 100%; text-align: center; font-size: 17px; }
  .card-front .wordmark { left: 40px; top: 100px; }
  .card-front .wordmark-dot { width: 34px; height: 34px; }
  .card-front .wordmark-name { font-size: 52px; }
  .contact-block { position: absolute; left: 325px; font-size: 12px; line-height: 19px; color: var(--ink-soft); }
  .contact-block b { color: var(--ink); }
  .contact-phones { top: 58px; }
  .contact-web { top: 160px; }
  .front-band { position: absolute; left: 0; bottom: 0; width: 100%; height: 120px; }
  .address { position: absolute; left: 40px; bottom: 30px; font-size: 12px; line-height: 17px; color: #fff; }
  .person { position: absolute; right: 30px; bottom: 40px; font-size: 13px; color: var(--ink-soft); }
  .person strong { font-size: 16px; color: var(--ink); }

  /* Back card */
  .card-back { left: 48px; top: 389px; width: 547px; height: 307px; }
  .card-back .company-title { top: 42px; left: 40px; font-size: 19px; }
  .card-back .wordmark { left: 54px; top: 118px; }
  .card-back .wordmark-dot { width: 36px; height: 36px; }
  .card-back .wordmark-name { font-size: 58px; }
  .back-contact { position: absolute; left: 40px; top: 244px; font-size: 15px; color: var(--ink); }
  .back-contact .divider { margin: 0 8px; }

  /* Services card */
  .card-services { left: 619px; top: 389px; width: 545px; height: 307px; }
  .services-title {
    position: absolute; top: 26px; width: 100%; text-align: center;
    font-size: 20px; font-weight: 700; color: var(--brand-blue);
  }
  .services-list {
    position: absolute; top: 62px; width: 100%;
    list-style: none; text-align: center; font-size: 15px; line-height: 29px; color: var(--ink);
  }
  .services-list li::before { content: "• "; }
</style>
</head>
<body>

<section class="card card-front" aria-label="Business card front">
  <h1 class="company-title">Harborline Biomedical Systems</h1>
  <div class="wordmark">
    <span class="wordmark-dot"></span>
    <span class="wordmark-name">halvorn</span>
  </div>
  <div class="contact-block contact-phones">
    <div><b>tf :</b> (800) 555-0142</div>
    <div><b>p :</b> (904) 555-0187</div>
    <div><b>f :</b> (904) 555-0123</div>
  </div>
  <div class="contact-block contact-web">
    <div><b>e :</b> derek.palmer@hb-sysmed.net</div>
    <div><b>w :</b> www.hb-sysmed.net</div>
  </div>
  <svg class="front-band" viewBox="0 0 516 120" preserveAspectRatio="none" aria-hidden="true">
    <defs>
      <linearGradient id="bandBlue" x1="0" y1="0" x2="1" y2="1">
        <stop offset="0" stop-color="#3aa7ea"/>
        <stop offset="1" stop-color="#0a5fa8"/>
      </linearGradient>
    </defs>
    <path d="M0 30 C150 10 300 20 516 60 L516 120 L0 120 Z" fill="#9fd3f5"/>
    <path d="M0 38 C160 22 300 40 420 120 L0 120 Z" fill="url(#bandBlue)"/>
    <path d="M290 80 C360 70 450 78 516 95 L516 120 L330 120 Z" fill="#f4f6f8"/>
  </svg>
  <p class="address">415 Wexmoor Avenue<br>Jacksonville, FL 32209</p>
  <p class="person"><strong>Derek Palmer</strong> - Vice President</p>
</section>

<section class="card card-back" aria-label="Business card back">
  <h2 class="company-title">Harborline Biomedical Systems</h2>
  <div class="wordmark">
    <span class="wordmark-dot"></span>
    <span class="wordmark-name">halvorn</span>
  </div>
  <p class="back-contact"><b>e</b> : derek.palmer@hb-sysmed.net<span class="divider">|</span><b>w</b> : www.hb-sysmed.net</p>
</section>

<section class="card card-services" aria-label="Services card">
  <h2 class="services-title">Our services</h2>
  <ul class="services-list">
    <li>Anesthesia Systems Maintenance</li>
    <li>Biomedical Equipment and Sterilization Maintenance</li>
    <li>Medical Gas Certification and Vacuum Pump Maintenance</li>
    <li>Pre-owned Equipment Sales</li>
    <li>Endoscopic Instrument Sales and Service</li>
    <li>Mobile Hand Instrument Maintenance</li>
    <li>Video Equipment Loaners and Service</li>
  </ul>
</section>

</body>
</html>
```